Box Design of "pet rapid test for dogs & cats" with professional use

"The market is in Southeast Asia, South America, Europe, and the U.S."
Clients: Veterinary clinics, pet hospitals,(a small number of home use)

Primary colors:
Orange, Green,or Blue, (select 1,or 2 color)
Neutrals: Black, Gray, or White (optional)
Dimensions:135mm(L)*90mm(W)*105mm(W)

Kindly review the attached file for additional content
Updates

I have increased my budget, please provide a satisfactory design solution, thank you very much for your work.

Target Market(s)

Southeast Asia, South America, Europe, and the U.S.

Industry/Entity Type

Veterinary test kit for dogs & cats

Colors
0054AA
0677BA
7BADD7
CADEEF
E8F1F8
0094D4
00A9DD
6FCCEA
C7EBF8
E9F6FB
00AB8E
00BBA5
67D7C9
C6EFE9
E9F9F6
59FF00
82FF00
B8FF75
E3FFCB
F4FFEA
F0912C
F2A743
F7CA91
FBE8D2
FDF5EE
EE7325
F08F49
F5BC92
FAE3D3
FDF4ED

Requirements
Nice to have
• Appealing Box Appearance with professional

```html
<!DOCTYPE html>
<html lang="en">
<head>
<meta charset="utf-8">
<title>PawTrace Pet Rapid Test Kit – Box Dieline</title>
<link rel="stylesheet" href="https://fonts.googleapis.com/css2?family=League+Gothic&family=Poppins:wght@400;500;600;700&display=swap">
<style>
:root{
  --green:#6c9c3b;
  --lime:#a3c614;
  --lime-text:#b6dd2a;
  --leaf:#7fae2e;
  --ink:#111;
  --paper:#fff;
  --dieline:#4a4a4a;
}
*{box-sizing:border-box;margin:0;padding:0}
html,body{width:1200px;height:730px;overflow:hidden;background:var(--paper)}
body{position:relative;font-family:"Poppins",sans-serif;color:var(--ink)}
.dieline{position:absolute;left:0;top:0}
.panel{position:absolute;top:306px;height:206px;overflow:hidden}
.panel--green{background:var(--green);color:#fff}
.panel--side-es{left:75px;width:192px}
.panel--front-en{left:267px;width:314px}
.panel--side-en{left:581px;width:193px}
.panel--front-es{left:774px;width:314px}
.brand{position:absolute;font-family:"Poppins",sans-serif;font-weight:700;font-size:15px;letter-spacing:-.2px;color:var(--ink)}
.abs{position:absolute}
.nowrap{white-space:nowrap}
.small-head{font-size:6px;font-weight:500}
.bullets{list-style:none;font-size:5px;line-height:7px}
.bullets li::before{content:"› ";color:var(--lime-text)}
.feature-box{position:absolute;left:14px;top:65px;width:164px;height:58px;background:var(--lime);color:var(--ink);padding:5px 6px;font-size:5px;line-height:6.8px}
.feature-box b{font-weight:600}
.condensed{font-family:"League Gothic",sans-serif;font-weight:400;white-space:nowrap}
.tagline{font-size:5px}
.headline{position:absolute;left:14px;font-family:"League Gothic",sans-serif;font-weight:400;color:var(--leaf);font-size:37px;line-height:31px;text-transform:uppercase;white-space:nowrap}
.subline{position:absolute;font-family:"League Gothic",sans-serif;font-weight:400;color:var(--ink);white-space:nowrap}
.rule{position:absolute;height:1px;background:#555}
.contents{position:absolute;left:14px;list-style:none;font-size:4.6px;line-height:6.2px}
.store{position:absolute;left:21px;font-family:"League Gothic",sans-serif;font-size:6px;white-space:nowrap}
.symbols{position:absolute;left:14px;display:flex;gap:7px;align-items:center}
.symbols span{font-size:4.5px;border:.6px solid #333;padding:0 2px;font-weight:600}
.symbols i{display:inline-block;width:7px;height:7px;border:.6px solid #333;border-radius:50%;font-style:normal;font-size:4.5px;text-align:center;line-height:6px}
.count-tag{position:absolute;background:var(--green);color:#fff;font-family:"League Gothic",sans-serif;font-size:9px;display:flex;align-items:center;justify-content:center;white-space:nowrap}
.illustration{position:absolute;background:linear-gradient(160deg,#f4f4f4,#dcdcdc);border-radius:8px}
.white-box{position:absolute;left:14px;top:83px;width:165px;height:54px;background:#fff;color:var(--ink);padding:6px 6px;font-size:4.5px;line-height:6px}
.white-box b{font-size:5.6px;font-weight:600;display:block;line-height:7px}
.lid{position:absolute;left:774px;top:114px;width:314px;height:192px;background:var(--green);display:flex;align-items:center;justify-content:center}
.lid .brand-large{font-family:"Poppins",sans-serif;font-weight:700;font-size:54px;color:#fff;letter-spacing:-1px}
</style>
</head>
<body>

<svg class="dieline" width="1200" height="730" viewBox="0 0 1200 730" fill="none" stroke="var(--dieline)" stroke-width=".6">
  <path d="M774 306 V90 Q774 67 797 67 H1065 Q1088 67 1088 90 V306"/>
  <path d="M80 306 V221 H240 Q257 221 257 245 L262 300 L267 306"/>
  <path d="M581 306 L586 300 L591 245 Q591 221 608 221 H769 V306"/>
  <path d="M1088 306 L1127 313 V506 L1088 512"/>
  <path d="M75 512 L171 576 V605 Q171 620 186 620 H267 V512"/>
  <path d="M267 512 L337 617 V649 Q337 664 352 664 H496 Q511 664 511 649 V617 L581 512"/>
  <path d="M581 512 V620 H663 Q678 620 678 605 V576 L774 512"/>
  <rect x="75" y="306" width="1013" height="206"/>
</svg>

<section class="lid" aria-label="Top lid">
  <span class="brand-large">PawTrace</span>
</section>

<!-- Side panel, Spanish -->
<section class="panel panel--green panel--side-es">
  <div class="brand" style="left:15px;top:12px">PawTrace</div>
  <div class="abs" style="left:14px;top:39px">
    <p class="small-head">Fácil y Práctico:</p>
    <ul class="bullets">
      <li>Sin capacitación previa</li>
      <li>Suficientemente simple para Para uso en casa</li>
    </ul>
  </div>
  <div class="feature-box">
    <b>RÁPIDO Y EFICIENTE:</b><br>
    Resultados digitales en &lt;10 minutos<br>
    Desde inicio hasta resultado final<br>
    <b>PRECISO Y FIABLE:</b><br>
    Resultados rápidos y confiables con tecnología de<br>
    inmunocromatografía avanzada<br>
    Validado por clínicas veterinarias a nivel global
  </div>
  <div class="abs" style="left:14px;top:130px">
    <p class="small-head" style="font-size:5.2px">DETECCIÓN MULTIENFERMEDADES:</p>
    <ul class="bullets">
      <li>Evalúa múltiples patologías simultáneamente</li>
      <li>Ayudar a los dueños de mascotas a detectar problemas<br>&nbsp;&nbsp;a tiempo</li>
    </ul>
  </div>
  <div class="abs condensed" style="left:14px;top:163px;font-size:19px">PawTrace</div>
  <div class="abs tagline" style="left:14px;top:190px">Loved by Pets, Trusted by Vets</div>
</section>

<!-- Front panel, English -->
<section class="panel panel--front-en">
  <div class="brand" style="left:14px;top:12px">PawTrace</div>
  <h1 class="headline" style="top:36px">Pet Rapid<br>Test Kit</h1>
  <div class="subline" style="left:14px;top:99px;font-size:21px">For Dogs &amp; Cats</div>
  <div class="rule" style="left:14px;top:127px;width:73px"></div>
  <ol class="contents" style="top:137px">
    <li>(1)&nbsp; Test Kits(Cassette,disposable<br>&nbsp;&nbsp;&nbsp;&nbsp;&nbsp;dropper,desiccant)</li>
    <li>(2)&nbsp; Assay buffer</li>
    <li>(3)&nbsp; Sterile swabs</li>
    <li>(4)&nbsp; Instruction manual.</li>
  </ol>
  <div class="store" style="top:168px">Store at 2–30c, Avoid direct sunlight</div>
  <div class="symbols" style="top:184px"><span>IVD</span><i>°</i><i>✳</i><i>▭</i><i>2</i></div>
  <div class="count-tag" style="left:97px;top:176px;width:34px;height:16px">10 Tests/Box</div>
  <div class="illustration" role="img" aria-label="Line illustration of a sitting dog with a collar" style="left:163px;top:31px;width:132px;height:161px"></div>
</section>

<!-- Side panel, English -->
<section class="panel panel--green panel--side-en">
  <div class="brand" style="left:13px;top:12px">PawTrace</div>
  <div class="abs condensed" style="left:13px;top:38px;font-size:21px">Rapid Test Kit</div>
  <div class="abs" style="left:14px;top:64px">
    <p class="small-head">Simple &amp; Convenient:</p>
    <p style="font-size:4.2px">No professional skills required,Simple enough for home use</p>
  </div>
  <div class="white-box">
    <b>Fast &amp; Efficient:</b>
    Digital results in &lt; 10 minutes - from start to completion.
    <b style="margin-top:6px">Accurate &amp; Reliable:</b>
    Quick and trustworthy pet health results using advanced lateral<br>flowbiotech,Trusted by vet clinics worldwide.
  </div>
  <p class="abs" style="left:14px;top:143px;font-size:5.6px;line-height:7px;color:var(--lime-text)">Supports screening of multiple diseases, Helping<br>pet owners detect issues early.</p>
  <div class="abs condensed" style="left:13px;top:162px;font-size:20px">MADE by NORAVET™</div>
  <div class="abs tagline" style="left:13px;top:190px">Loved by Pets, Trusted by Vets</div>
</section>

<!-- Front panel, Spanish -->
<section class="panel panel--front-es">
  <div class="brand" style="left:13px;top:12px">PawTrace</div>
  <h1 class="headline" style="top:36px;left:13px;font-size:35px;line-height:30px">Kit de prueba<br>rápida para mascotas</h1>
  <div class="subline" style="left:13px;top:98px;font-size:17px">Querido por las mascotas, confiado por veterinarios</div>
  <div class="rule" style="left:13px;top:122px;width:142px"></div>
  <ol class="contents" style="top:134px;left:13px">
    <li>(1)&nbsp; Kits de prueba (cassette, gotero<br>&nbsp;&nbsp;&nbsp;&nbsp;&nbsp;desechable, desecante)</li>
    <li>(2)&nbsp; Buffer de ensayo</li>
    <li>(3)&nbsp; Hisopos estériles</li>
    <li>(4)&nbsp; Manual de instrucciones</li>
  </ol>
  <div class="store" style="top:165px">Almacenamiento: 2–30c</div>
  <div class="symbols" style="top:183px;left:13px"><span>IVD</span><i>°</i><i>✳</i><i>▭</i><i>2</i></div>
  <div class="count-tag" style="left:97px;top:175px;width:34px;height:16px;font-size:6.5px">10 pruebas por caja</div>
  <div class="illustration" role="img" aria-label="Line illustration of a small corgi dog with a drip bag doodle" style="left:212px;top:120px;width:84px;height:74px"></div>
</section>

</body>
</html>
```